Business infographic - project management

We welcome agencies and artists to come up with their own concept if they feel they have an idea that is way more effective at communicating the role and relationship of our company between client and all other catagories.

it can be completely different, or you can simply refine the current example we have provided.

The intention is to use this graphic to simplify how are services are different to other deliveries methods (others being design-build, or design-bid-build) Attached is our preliminary idea, to show the relationship between our company, client and all other stake holder groups.

here is a company intro:
Since 2007, Velmoric construction & project management has evolved from a drafting and design firm into your single-source solution for project delivery. We transcend traditional EPCM services (engineering, procurement, construction management) by offering comprehensive project management tailored to your design-build needs. Our involvement begins as early as property evaluations and business case development, ensuring your project is guided by a clear vision and a commitment to maximizing value.
We act as your dedicated project manager, aligning your vision, values, and constraints while safeguarding your interests. Our approach uncovers hidden opportunities for benefits and savings that go directly back to you, the client.

What This Means for You:
• Avoids compounding markups and incentivizes higher performance from vendors and trades.
• Aligns every project with your strategic goals and objectives.
• Uncovers overlooked features to enhance functionality and value.
• Prioritizes lifecycle considerations, including usage, enjoyment, and safety.
• Crafts designs optimized for time, budget, and quality constraints.
• Minimizes miscommunication to prevent costly mistakes.
• Eliminates inefficiencies and unnecessary learning curves.
• Ensures value engineering savings go directly to you.
Our core focus is on projects with user-specific requirements, bringing together collaborative teams to foster partnerships that align owners, consultants, and subcontractors with a win-win approach. This method ensures the most positive, motivated, and complete project outcomes.

Why Choose Velmoric?
We bring developer-inspired efficiencies to every project, blending expertise with passion to unlock unparalleled value. With transparent communication and proactive management, we deliver seamless results while safeguarding your bottom line. At Velmoric, we’re not just managing projects—we’re building lasting partnerships and transforming visions into reality.

Target Market(s)

Commercial & Residential construction

Industry/Entity Type

Construction & Project Management

Font styles to use
Sans Serif

Colors

Designer to choose colors to be used in the design.

Requirements
Nice to have
• 3D views, playful look that might be appealing to residential clients

```html
<!DOCTYPE html>
<html lang="en">
<head>
<meta charset="utf-8">
<title>Developer-Emulated Project Manager (DEPM) – Velmoric</title>
<link href="https://fonts.googleapis.com/css2?family=Barlow+Condensed:wght@500;600;700&display=swap" rel="stylesheet">
<style>
:root{
  --frame:#30333b;
  --green-dark:#3f7d32;
  --green-light:#6abf4b;
  --pale:#e6f0e3;
  --disc:#e3eee0;
  --white:#ffffff;
}
*{margin:0;padding:0;box-sizing:border-box}
html,body{width:875px;height:1200px;overflow:hidden;background:var(--frame)}
body{font-family:"Barlow Condensed",sans-serif;position:relative}
.sheet{position:absolute;left:17px;top:16px;width:842px;height:1030px;background:var(--white)}
.links{position:absolute;left:0;top:0;width:875px;height:1050px}
.disc{position:absolute;width:112px;height:112px;border-radius:50%;
  background:radial-gradient(circle at 50% 45%,#d3e6cd 0%,var(--disc) 70%)}
.pill{position:absolute;height:23px;border-radius:12px;background:var(--green-dark);color:var(--white);
  font-weight:700;font-size:17px;line-height:23px;text-align:center;letter-spacing:.1px;white-space:nowrap}
.tasks{position:absolute;background:var(--pale);list-style:none;color:var(--green-dark);
  font-weight:500;font-size:10px;padding-top:3px}
.tasks li{position:relative;white-space:nowrap}
.tasks li::before{content:"";position:absolute;left:-14px;top:5px;width:5px;height:5px;background:var(--green-dark)}
.hub{position:absolute;left:356px;top:379px;width:166px;height:144px}
.hub-name{position:absolute;left:356px;top:444px;width:166px;text-align:center;color:var(--white);
  font-weight:600;font-size:17px;letter-spacing:3px}
.hub-mark{position:absolute;left:429px;top:418px;width:20px;height:20px;background:var(--white)}
.note{position:absolute;right:38px;top:1028px;font-size:12.5px;font-weight:500;color:var(--frame)}
.title{position:absolute;left:0;top:1057px;width:875px;text-align:center;color:var(--white);
  font-weight:700;font-size:39px;letter-spacing:.3px}
.tagline{position:absolute;left:0;top:1112px;width:875px;text-align:center;color:var(--white);
  font-weight:600;font-size:16px;line-height:24px}
.brand{position:absolute;left:34px;top:1170px;color:var(--white);font-weight:600;font-size:14px;letter-spacing:2px}
.brand-mark{position:absolute;left:64px;top:1130px;width:30px;height:30px;background:var(--white)}
</style>
</head>
<body>
<div class="sheet"></div>

<svg class="links" viewBox="0 0 875 1050" aria-hidden="true">
  <defs>
    <marker id="head-dark" viewBox="0 0 10 10" refX="8" refY="5" markerWidth="5" markerHeight="5" orient="auto-start-reverse">
      <path d="M0,0 L10,5 L0,10 z" fill="#3f7d32"/>
    </marker>
    <marker id="head-light" viewBox="0 0 10 10" refX="8" refY="5" markerWidth="5" markerHeight="5" orient="auto-start-reverse">
      <path d="M0,0 L10,5 L0,10 z" fill="#6abf4b"/>
    </marker>
  </defs>
  <g fill="none" stroke-width="2">
    <!-- owner ↔ hub -->
    <path d="M440 233 V190" stroke="#3f7d32" marker-end="url(#head-dark)"/>
    <path d="M440 335 V372" stroke="#3f7d32" marker-end="url(#head-dark)"/>
    <!-- lender ↔ owner, realtor ↔ owner -->
    <path d="M257 232 C280 170 320 140 373 143" stroke="#6abf4b" marker-start="url(#head-light)" marker-end="url(#head-light)"/>
    <path d="M627 232 C604 170 564 140 511 143" stroke="#6abf4b" marker-start="url(#head-light)" marker-end="url(#head-light)"/>
    <!-- owner ↔ hub side arcs -->
    <path d="M310 160 C300 250 320 330 383 390" stroke="#3f7d32" marker-start="url(#head-dark)" marker-end="url(#head-dark)"/>
    <path d="M568 160 C578 250 558 330 498 390" stroke="#3f7d32" marker-start="url(#head-dark)" marker-end="url(#head-dark)"/>
    <!-- hub ↔ consultants, trades -->
    <path d="M354 458 C330 510 290 535 245 541" stroke="#3f7d32" marker-start="url(#head-dark)" marker-end="url(#head-dark)"/>
    <path d="M524 458 C548 510 588 535 633 541" stroke="#3f7d32" marker-start="url(#head-dark)" marker-end="url(#head-dark)"/>
    <!-- hub ↔ site -->
    <path d="M440 543 V528" stroke="#3f7d32" marker-end="url(#head-dark)"/>
    <path d="M440 625 V646" stroke="#3f7d32" marker-end="url(#head-dark)"/>
    <!-- trades ↔ site -->
    <path d="M628 605 C590 660 540 688 482 691" stroke="#6abf4b" marker-start="url(#head-light)" marker-end="url(#head-light)"/>
    <!-- sub traders → site -->
    <path d="M439 861 V836" stroke="#3f7d32" marker-end="url(#head-dark)"/>
    <!-- hub ↔ sub traders loop -->
    <path d="M391 526 C370 535 345 543 322 543 V863 C345 863 365 870 379 882" stroke="#6abf4b" marker-start="url(#head-light)" marker-end="url(#head-light)"/>
  </g>
  <g fill="none" stroke="#3f7d32" stroke-width="1.2" stroke-dasharray="3 3">
    <path d="M248 365 H332 V320"/>
    <path d="M248 460 H331 V500"/>
    <path d="M546 326 V344 H593"/>
    <path d="M593 437 H546 V498"/>
    <path d="M286 736 H318"/>
  </g>
</svg>

<!-- hub -->
<svg class="hub" viewBox="0 0 166 144" aria-hidden="true">
  <polygon points="0,72 36,0 130,0 166,72 130,144 36,144" fill="#3f7d32"/>
</svg>
<div class="hub-mark"></div>
<div class="hub-name">VELMORIC</div>

<!-- stakeholders -->
<div class="disc" style="left:381px;top:71px" role="img" aria-label="Illustration of the owner standing"></div>
<div class="pill" style="left:405px;top:43px;width:64px">OWNER</div>

<div class="disc" style="left:137px;top:193px" role="img" aria-label="Illustration of a bank building with stacks of money"></div>
<div class="pill" style="left:158px;top:311px;width:69px">LENDER</div>

<div class="disc" style="left:633px;top:196px" role="img" aria-label="Illustration of a house with a realtor beside it"></div>
<div class="pill" style="left:648px;top:311px;width:82px">REALTOR</div>

<div class="disc" style="left:124px;top:519px" role="img" aria-label="Illustration of an architect, engineer and consultant talking"></div>
<div class="pill" style="left:53px;top:638px;width:254px">ARCHITECT, ENGINEER &amp; CONSULTANTS</div>

<div class="disc" style="left:641px;top:519px" role="img" aria-label="Illustration of tradespeople at a supply counter with a laptop"></div>
<div class="pill" style="left:605px;top:638px;width:182px">MAJOR TRADES &amp; SUPPLIES</div>

<div class="disc" style="left:383px;top:691px" role="img" aria-label="Illustration of site workers in hard hats under a crane"></div>
<div class="pill" style="left:347px;top:808px;width:183px">SITE SUPERVISION &amp; SAFETY</div>

<div class="disc" style="left:383px;top:866px" role="img" aria-label="Illustration of a delivery truck being unloaded by workers"></div>
<div class="pill" style="left:351px;top:983px;width:175px">SUB TRADERS &amp; VENDORS</div>

<!-- task lists -->
<ul class="tasks" style="left:370px;top:238px;width:139px;height:97px;padding-left:6px">
  <li style="height:12.9px">Define goals &amp; objectives</li>
  <li style="height:12.9px">Feasibility study</li>
  <li style="height:12.9px">Operation &amp; maintenance outlook</li>
  <li style="height:12.9px">Initial concepts</li>
  <li style="height:12.9px">Value engineering &amp; solutions</li>
  <li style="height:12.9px">Define requirements &amp; constraints</li>
  <li style="height:12.9px">Develop project budget &amp; schedule</li>
</ul>

<ul class="tasks" style="left:80px;top:342px;width:168px;height:49px;padding-left:7px">
  <li style="height:13.5px">Provide construction budget</li>
  <li style="height:14.5px">Sipplement application with project details</li>
  <li>Avoid delays when releasing funds</li>
</ul>

<ul class="tasks" style="left:80px;top:421px;width:168px;height:65px;padding-left:7px">
  <li style="height:14.8px">Protect objectives and constraints</li>
  <li style="height:14.8px">Avoid error and conflicting info</li>
  <li style="height:14.8px">Avoid unnecessary cost &amp; complexity</li>
  <li>Accelerate drawing packages</li>
</ul>

<ul class="tasks" style="left:593px;top:342px;width:204px;height:69px;padding-left:7px">
  <li style="height:14.4px">Identify property risks and challenges</li>
  <li style="height:14.4px">Audit property against project goals &amp; objectives</li>
  <li style="height:14.4px">Cut &amp; fill assessment</li>
  <li>Conceptual layouts &amp; operational performance</li>
</ul>

<ul class="tasks" style="left:593px;top:436px;width:204px;height:64px;padding-left:6px">
  <li style="height:14.3px">Assist with best value design &amp; methodology</li>
  <li style="height:14.3px">Identify risks and opportunities</li>
  <li style="height:14.3px">Provide topic expertise and value engineering input</li>
  <li>Provide options for best value products and finishes</li>
</ul>

<ul class="tasks" style="left:342px;top:558px;width:217px;height:67px;padding-left:4px">
  <li style="height:15.3px">Research &amp; compatibility with safety &amp; bylaw regulations</li>
  <li style="height:15.3px">Appoint full time safety office</li>
  <li style="height:15.3px">Audit sub trade qualifications and safety</li>
  <li>Verify adequate insuarance coverages</li>
</ul>

<ul class="tasks" style="left:80px;top:703px;width:206px;height:73px;padding-left:7px">
  <li style="height:16.5px">Coordinate between trade and disciplines</li>
  <li style="height:16.5px">Remove soope gaps or overlaps</li>
  <li style="height:16.2px">Solicit feedback regarding compatibility of design</li>
  <li>Provide options for best value products and finishes</li>
</ul>

<div class="note">Note: All are purchased vectors in our design</div>

<h1 class="title">DEVELOPER-EMULATED PROJECT MANAGER (DEPM)</h1>
<p class="tagline">EMPOWERING CLIENTS TO ACHIEVE PROJECT SUCCESS THROUGH<br>A STREAMLINED VALUE-DRIVEN PARTNERSHIP APPROACH,<br>RETURNING ANY BENEFITS ORS SAVINGS BACK TO THE OWNER</p>

<div class="brand-mark"></div>
<div class="brand">VELMORIC</div>
</body>
</html>
```